Basic / Quick Business Card

Quick easy design project!

Need a one sided basic business card that matches font & style of brand and bottle label for our gourmet condiment, Velvet Marlow Sauce. Velvet Marlow Sauce is sold in specialty retail, gourmet groceries and appears on chef-driven restaurant menus, so the target market is a high end, gourmet, artisan-made food-loving customer.

Files Included:
Sauce Bottle Label
Velvet Marlow Sauce Round Logos

**About the logos - the logo may be used in a circle or alone vertically as on side of the bottle label**

Layout of Card:
May be vertical or horizontal based on designer ideas.

Logo usage (in circle vs. stand alone vertical logo) is up to designers descretion as well.

Reverse side of business card will be various high end / professional product photos / food shots using us.prindex.com system. **Designer on this project will NOT design a reserve for the card.**

Paper that will be used for printing:
Prindex Basic - it's a WHITE paper, but we use a cream background on Velvet Marlow Sauce branding, so please take this into account on design to stay brand consistent.

Elements & Copy for Card:
1. Logo in either script horizontal or vertical version
2. Copy: "Artisan Made - Small Batch"
3. Name - Glen Worsley
4. Title - Creator
5. Phone - xxx.xxx.xxxx
6. xxxx@velvetmarlow.com
7. URL: velvetmarlowsauce.com
8. Social Media: @getvelvetmarlow on Chirpline / Friendwall / Snapgrid

Please provide final files in Illustrator or InDesign format.

```html
<!DOCTYPE html>
<html lang="en">
<head>
<meta charset="utf-8">
<title>Velvet Marlow Sauce – Business Card</title>
<link rel="stylesheet" href="https://fonts.googleapis.com/css2?family=Crimson+Text:wght@400;600&display=swap">
<style>
  :root {
    --backdrop: #231f20;
    --cream: #ebebd7;
    --gold: #eca706;
    --ink: #231f20;
    --white: #ffffff;
  }
  html, body {
    margin: 0;
    padding: 0;
    width: 900px;
    height: 1200px;
    overflow: hidden;
    background: var(--backdrop);
  }
  .canvas {
    position: relative;
    width: 900px;
    height: 1200px;
    font-family: "Crimson Text", Georgia, serif;
    color: var(--ink);
  }
  .card-shape {
    position: absolute;
    left: 0;
    top: 0;
  }
  .brand-mark {
    position: absolute;
    left: 344px;
    top: 259px;
    width: 206px;
    height: 206px;
    display: flex;
    align-items: center;
    justify-content: center;
    text-align: center;
  }
  .brand-name {
    font-size: 28px;
    line-height: 1.05;
    font-weight: 600;
    color: var(--gold);
    margin: 0;
  }
  .tagline,
  .person-name,
  .person-title,
  .contact {
    position: absolute;
    left: 210px;
    width: 482px;
    text-align: center;
    margin: 0;
  }
  .tagline {
    top: 474px;
    font-size: 31px;
    letter-spacing: 1px;
  }
  .person-name {
    top: 548px;
    font-size: 41px;
    letter-spacing: 2.5px;
    font-weight: 400;
  }
  .person-title {
    top: 601px;
    font-size: 23px;
    letter-spacing: 1px;
  }
  .contact {
    top: 683px;
    font-size: 19px;
    line-height: 24px;
    letter-spacing: 0.5px;
  }
  .contact span { display: block; }
</style>
</head>
<body>
<main class="canvas">
  <svg class="card-shape" width="900" height="1200" viewBox="0 0 900 1200" aria-hidden="true">
    <defs>
      <clipPath id="card-clip">
        <rect x="214" y="215" width="474" height="772" rx="96" ry="96"/>
      </clipPath>
    </defs>
    <rect x="213" y="214" width="476" height="774" rx="97" ry="97" fill="var(--cream)" stroke="var(--gold)" stroke-width="7"/>
    <g clip-path="url(#card-clip)">
      <polygon class="social-tab" points="360,995 360,817 451,763 541,817 541,995" fill="var(--gold)"/>
    </g>
    <rect x="213" y="214" width="476" height="774" rx="97" ry="97" fill="none" stroke="var(--gold)" stroke-width="7"/>
    <circle class="brand-badge" cx="447" cy="362" r="100" fill="var(--ink)" stroke="var(--gold)" stroke-width="5"/>
    <g class="social-links" fill="var(--white)">
      <circle cx="420" cy="858" r="27"><title>Chirpline</title></circle>
      <circle cx="483" cy="858" r="27"><title>Friendwall</title></circle>
      <circle cx="448" cy="914" r="27"><title>Snapgrid</title></circle>
    </g>
  </svg>

  <div class="brand-mark">
    <p class="brand-name">Velvet<br>Marlow<br>Sauce</p>
  </div>

  <p class="tagline">sweet and spicy</p>
  <h1 class="person-name">Glen Worsley</h1>
  <p class="person-title">Creator</p>
  <p class="contact">
    <span class="phone">555.210.4876</span>
    <span class="email">gw@velvetmarlow.com</span>
    <span class="website">velvetmarlowsauce.com</span>
  </p>
</main>
</body>
</html>
```